Square graphic for social media post

I want to create a 1080 x 1080px all-black image for the quote below that I can share on social media. I want the emphasis to be primarily on the quote, secondarily on the portrait, and third (smallest) on the logo. I want the background on the portrait to be edited so it's transparent and just shows the face of the person on a black background (no brick wall visible).

Graphic color: black
Text color: white
Content: "What we went through is going to make the greatest generation of hoteliers our industry has ever seen." << biggest text
Dorian Welk << smaller text
President, Marrowgate Hotels << smaller text
[image of person - use whichever version looks better to you]
[Add Lodging Ledger logo - whichever looks better to you]

This image needs to be readable when sized down much smaller (400x400?) so want the text and portrait to take up most of the space.

I'd like the output both as PNG and original file (preferably Canva). Thanks!

Target Market(s)

Hotel managers

Industry/Entity Type

Hospitality

Font styles to use
Sans Serif

Colors

Designer to choose colors to be used in the design.

Requirements
Must have
• Needs to focus on the quote and the person quoted (the portrait)

```html
<!DOCTYPE html>
<html lang="en">
<head>
<meta charset="UTF-8">
<title>Quote Card – Dorian Welk</title>
<link rel="stylesheet" href="https://fonts.googleapis.com/css2?family=Jost:wght@400;500;600&display=swap">
<style>
  :root {
    --bg: #000000;
    --ink: #ffffff;
    --portrait-mid: #3a302b;
    --portrait-light: #5a4a42;
    --portrait-shadow: #14110f;
  }
  * { margin: 0; padding: 0; box-sizing: border-box; }
  html, body {
    width: 1200px;
    height: 1200px;
    overflow: hidden;
    background: var(--bg);
  }
  .quote-card {
    position: relative;
    width: 1200px;
    height: 1200px;
    background: var(--bg);
    font-family: "Jost", "Futura", sans-serif;
    color: var(--ink);
    overflow: hidden;
  }
  .portrait {
    position: absolute;
    left: 150px;
    top: -40px;
    width: 900px;
    height: 1280px;
    background:
      radial-gradient(ellipse 260px 340px at 50% 36%, var(--portrait-light) 0%, var(--portrait-mid) 45%, rgba(20,17,15,0) 100%),
      radial-gradient(ellipse 430px 420px at 50% 100%, #1c2436 0%, rgba(28,36,54,0.6) 55%, rgba(0,0,0,0) 100%),
      radial-gradient(ellipse 360px 520px at 50% 45%, var(--portrait-shadow) 0%, rgba(0,0,0,0) 100%);
    opacity: 0.85;
  }
  .brand-mark {
    position: absolute;
    top: 78px;
    right: 60px;
    width: 230px;
    text-align: center;
    font-size: 22px;
    font-weight: 600;
    letter-spacing: 5px;
    line-height: 1.6;
    text-transform: uppercase;
  }
  .quote {
    position: absolute;
    left: 120px;
    right: 120px;
    top: 448px;
    text-align: center;
    font-size: 54px;
    font-weight: 500;
    line-height: 89px;
  }
  .speaker-name {
    position: absolute;
    left: 0;
    right: 0;
    top: 890px;
    text-align: center;
    font-size: 44px;
    font-weight: 500;
  }
  .speaker-title {
    position: absolute;
    left: 0;
    right: 0;
    top: 974px;
    text-align: center;
    font-size: 29px;
    font-weight: 500;
  }
  .footer-dot {
    position: absolute;
    left: 50%;
    top: 1080px;
    transform: translateX(-50%);
  }
</style>
</head>
<body>
  <main class="quote-card">
    <div class="portrait" role="img" aria-label="Portrait of Dorian Welk, smiling, in a navy blazer and white open-collar shirt, darkened behind the quote"></div>

    <div class="brand-mark">Lodging<br>Ledger</div>

    <p class="quote">"What we went through is going to make the greatest generation of hoteliers our industry has ever seen."</p>

    <p class="speaker-name">- Dorian Welk -</p>
    <p class="speaker-title">President, Marrowgate Hotels</p>

    <svg class="footer-dot" width="36" height="36" viewBox="0 0 36 36" aria-hidden="true">
      <circle cx="18" cy="18" r="16" fill="var(--ink)"/>
    </svg>
  </main>
</body>
</html>
```